Harvest Smokehouse League

The current website is hslsmoke.com. We want to change the color scheme to the gold/white and black in the logo. Front page elements include everything we have except the social media links at the top can go to the bottom. We need to add fliers like http://hslsmoke.com/content/fliers/2022/SmartSelect_20211215-123241_Slides.jpg to the front page. There are more available on the events page. Also a place for a main news story on the front page. All the sponsor logos need to be present on every page. I have added a couple of more sponsor logos. On the about us page we will want to add a contact list and email form. We will take care of all functionality. You provide only design.
One site we like is tpgr.us for it is easy to navigate.
Target Market(s)
People interested in competition BBQ
Coding
Number of Pages Required
5+ page
Look and feel

```html
<!DOCTYPE html>
<html lang="en">
<head>
<meta charset="utf-8">
<title>About Us – Harvest Smokehouse League</title>
<link rel="stylesheet" href="https://fonts.googleapis.com/css2?family=Montserrat:wght@500;700&family=Questrial&display=swap">
<style>
  :root {
    --gold: #dbc75a;
    --gold-soft: #e3cf5f;
    --header-bg: #f2f2f2;
    --page-bg: #eaeaea;
    --ink: #2f2f2f;
    --footer-left: #222222;
    --footer-right: #303030;
    --white: #ffffff;
  }
  * { margin: 0; padding: 0; box-sizing: border-box; }
  html, body { width: 1200px; height: 2194px; overflow: hidden; }
  body {
    position: relative;
    background: var(--page-bg);
    font-family: "Questrial", sans-serif;
    color: var(--ink);
  }
  .site-header {
    position: absolute; left: 0; top: 0; width: 1200px; height: 234px;
  }
  .site-header svg { position: absolute; left: 0; top: 0; }
  .brand {
    position: absolute; left: 0; width: 1200px; top: 52px;
    display: flex; justify-content: center; align-items: center; gap: 12px;
  }
  .brand-name {
    font-family: "Montserrat", sans-serif; font-weight: 500;
    font-size: 27px; letter-spacing: 2px; color: var(--gold);
  }
  .brand-dot { width: 30px; height: 30px; border-radius: 50%; background: var(--gold); }
  .main-nav {
    position: absolute; top: 145px; left: 141px;
    display: flex; gap: 0; font-size: 12px; letter-spacing: 3px; color: var(--ink);
  }
  .main-nav a { color: inherit; text-decoration: none; position: absolute; white-space: nowrap; }
  .section-title {
    position: absolute; left: 67px;
    font-family: "Montserrat", sans-serif; font-weight: 700;
    font-size: 28px; letter-spacing: 4px; color: var(--ink);
  }
  .section-lead {
    position: absolute; left: 67px; font-size: 17px; letter-spacing: 2px;
  }
  .about-copy {
    position: absolute; left: 67px; top: 474px; width: 700px;
    font-size: 16.5px; letter-spacing: 2px; line-height: 27.8px;
  }
  .team-card {
    position: absolute; width: 278px; height: 339px; background: var(--gold);
    text-align: center;
  }
  .team-photo {
    position: absolute; left: 78px; top: 67px; width: 122px; height: 122px;
    border-radius: 50%;
    background: radial-gradient(circle at 60% 40%, #f0e6d6 0%, #b8b0a4 55%, #3a3a38 100%);
  }
  .team-name {
    position: absolute; left: 0; width: 100%; top: 220px;
    font-size: 16px; letter-spacing: 2px; color: #3c3a2a;
  }
  .team-role {
    position: absolute; left: 0; width: 100%; top: 254px;
    font-size: 14px; letter-spacing: 1.6px; color: #2a2818;
  }
  .site-footer { position: absolute; left: 0; top: 1794px; width: 1200px; height: 400px; }
  .footer-about {
    position: absolute; left: 0; top: 0; width: 613px; height: 400px;
    background: var(--footer-left); color: var(--white);
    padding: 74px 0 0 68px; font-size: 14px; letter-spacing: 1.2px; line-height: 25.5px;
    font-family: "Montserrat", sans-serif; font-weight: 500;
  }
  .footer-contact {
    position: absolute; left: 613px; top: 0; width: 587px; height: 400px;
    background: var(--footer-right); color: var(--white);
    font-family: "Montserrat", sans-serif; font-weight: 500; font-size: 14px; letter-spacing: 1.2px;
  }
  .contact-line { position: absolute; left: 0; width: 517px; text-align: center; }
  .newsletter-title {
    position: absolute; left: 120px; top: 250px; color: var(--gold);
    font-weight: 700; font-size: 13.5px; letter-spacing: 1.5px;
  }
  .newsletter-field {
    position: absolute; left: 104px; top: 287px; width: 211px; height: 44px;
    border-radius: 22px; background: var(--white);
  }
  .newsletter-field span {
    position: absolute; left: 32px; top: 14px; font-size: 11px; color: #aaa; letter-spacing: 1px;
  }
  .newsletter-submit {
    position: absolute; right: 0; top: 0; width: 44px; height: 44px;
    border-radius: 50%; background: var(--gold-soft);
  }
</style>
</head>
<body>
  <header class="site-header">
    <svg width="1200" height="234" viewBox="0 0 1200 234" aria-hidden="true">
      <path d="M0 0H1200V197H745L600 233L455 197H0Z" fill="#f2f2f2"/>
    </svg>
    <div class="brand"><span class="brand-name">HARVEST SMOKEHOUSE LEAGUE</span><span class="brand-dot"></span></div>
    <nav class="main-nav">
      <a style="left:0">HOME</a>
      <a style="left:108px">EVENTS</a>
      <a style="left:232px">RESULTS</a>
      <a style="left:365px">TEAM OF THE YEAR</a>
      <a style="left:587px">ABOUT HSL</a>
      <a style="left:745px">SANCTIONING FORM</a>
    </nav>
  </header>

  <main>
    <h1 class="section-title" style="top:370px">ABOUT US</h1>
    <p class="section-lead" style="top:416px">We are HSL - Cooking competion holders</p>
    <p class="about-copy">Lorem ipsum dolor sit amet, consectetur adipiscing elit, sed<br>do eiusmod tempor incididunt ut labore et dolore magna aliqua.<br>Quis ipsum suspendisse ultrices gravida. Risus commodo<br>viverra maecenas accumsan lacus vel facilisis. Pellentesque nisl<br>magna, dictum sit amet mollis eget, placerat ac orci.<br>Donec orci ipsum, tincidunt in vestibulum sit amet, bibendum<br>ut lectus.</p>

    <h2 class="section-title" style="top:758px">OUR TEAM</h2>
    <p class="section-lead" style="top:804px">Get to know more about the team behind all this</p>

    <section class="team-grid">
      <article class="team-card" style="left:67px;top:881px"><div class="team-photo" role="img" aria-label="Portrait of team member at his desk"></div><p class="team-name">Dale Brooks</p><p class="team-role">Our Developer and coder</p></article>
      <article class="team-card" style="left:461px;top:881px"><div class="team-photo" role="img" aria-label="Portrait of team member at his desk"></div><p class="team-name">Dale Brooks</p><p class="team-role">Our Developer and coder</p></article>
      <article class="team-card" style="left:854px;top:881px"><div class="team-photo" role="img" aria-label="Portrait of team member at his desk"></div><p class="team-name">Dale Brooks</p><p class="team-role">Our Developer and coder</p></article>
      <article class="team-card" style="left:67px;top:1287px"><div class="team-photo" role="img" aria-label="Portrait of team member at his desk"></div><p class="team-name">Dale Brooks</p><p class="team-role">Our Developer and coder</p></article>
      <article class="team-card" style="left:461px;top:1287px"><div class="team-photo" role="img" aria-label="Portrait of team member at his desk"></div><p class="team-name">Dale Brooks</p><p class="team-role">Our Developer and coder</p></article>
      <article class="team-card" style="left:854px;top:1287px"><div class="team-photo" role="img" aria-label="Portrait of team member at his desk"></div><p class="team-name">Dale Brooks</p><p class="team-role">Our Developer and coder</p></article>
    </section>
  </main>

  <footer class="site-footer">
    <div class="footer-about">
      Harvest Smokehouse League is an organization founded by<br>barbecue cooks for barbecue cooks and our main goal<br>is to bring competition barbecue out of the stone age and<br>into the information age...<br>but above all we want to make barbecue fun again!
    </div>
    <div class="footer-contact">
      <p class="contact-line" style="top:71px">Call us</p>
      <p class="contact-line" style="top:97px">(555) 014-2837</p>
      <p class="contact-line" style="top:148px">Address</p>
      <p class="contact-line" style="top:173px">1870 Cedar Hollow Rd, Millbrook, TX 70000</p>
      <p class="newsletter-title">GET INFORMED</p>
      <div class="newsletter-field"><span>Email...</span><div class="newsletter-submit"></div></div>
    </div>
  </footer>
</body>
</html>
```